Crestline Gas and Plumbing Business Card Design

I am after a business card design for my plumbing business called 'Crestline Gas & Plumbing'. I do all types of plumbing and gas work and specialise in general maintenance plumbing. Would like to see designs using current logo

Industry/Entity Type

Plumbing

Contact Information for Business Card

Name - Dale Whitcombe
Phone number - 0455163027
Email - admin@crestlinegasandplumbing.example.com.au
ABN - 68204915336

```html
<!DOCTYPE html>
<html lang="en">
<head>
<meta charset="utf-8">
<title>Crestline Gas &amp; Plumbing – Business Card</title>
<link href="https://fonts.googleapis.com/css2?family=Cabin:wght@500&family=Roboto+Condensed:wght@400&family=Tinos&family=Archivo+Black&display=swap" rel="stylesheet">
<style>
  :root {
    --sheet: #ffffff;
    --frame: #1a1a1a;
    --brand-blue: #1746ff;
    --pipe-blue: #4a80ff;
    --pipe-grey: #e4e4e4;
    --ink: #111111;
    --accent-orange: #f47a1a;
    --link-blue: #1d5be0;
  }
  * { box-sizing: border-box; margin: 0; padding: 0; }
  html, body { width: 943px; height: 1200px; overflow: hidden; background: var(--sheet); }
  .sheet {
    position: relative; width: 943px; height: 1200px;
    border: 1.5px solid var(--frame); background: var(--sheet);
  }
  .card {
    position: absolute; left: 21px; width: 900px; height: 545px;
    border: 1.5px solid var(--frame); overflow: hidden;
  }
  .card--front { top: 31px; background: var(--brand-blue); }
  .card--back { top: 623px; background: var(--sheet); }

  .pipe-art { position: absolute; }
  .card--front .pipe-art {
    left: 0; top: 0; width: 654px; height: 545px;
    background: radial-gradient(ellipse at 55% 55%, rgba(74,128,255,0.75) 0%, rgba(74,128,255,0.35) 50%, rgba(74,128,255,0) 72%);
  }
  .card--back .pipe-art {
    left: 278px; top: 0; width: 622px; height: 545px;
    background: radial-gradient(ellipse at 60% 55%, rgba(228,228,228,0.9) 0%, rgba(228,228,228,0.45) 50%, rgba(228,228,228,0) 72%);
  }

  .brand-mark {
    position: absolute; display: flex; align-items: center; gap: 12px;
    font-family: "Archivo Black", sans-serif; font-size: 24px; line-height: 1.1;
    text-transform: uppercase; letter-spacing: 0.5px;
  }
  .brand-mark__dot { width: 40px; height: 40px; border-radius: 50%; flex: none; background: var(--accent-orange); }
  .brand-mark__name { display: block; }
  .card--front .brand-mark { left: 494px; top: 92px; color: #ffffff; }
  .card--back .brand-mark { left: 473px; top: 78px; color: var(--brand-blue); }

  .contact-name {
    position: absolute; left: 69px; top: 72px;
    font-family: "Cabin", sans-serif; font-weight: 500; font-size: 34px; color: var(--ink);
  }
  .contact-phone, .tagline, .details {
    position: absolute; left: 69px;
    font-family: "Roboto Condensed", sans-serif; color: var(--ink);
  }
  .contact-phone { top: 123px; font-size: 25px; }
  .business-name {
    position: absolute; left: 67px; top: 308px;
    font-family: "Tinos", serif; font-weight: 400; font-size: 41px; color: var(--link-blue);
    border-bottom: 3px solid var(--accent-orange); line-height: 1.05;
  }
  .tagline { top: 370px; font-size: 25px; line-height: 32px; }
  .details { top: 456px; font-size: 25px; line-height: 36px; }
</style>
</head>
<body>
<main class="sheet">
  <section class="card card--front">
    <div class="pipe-art" role="img" aria-label="Illustration of plumbing pipes leading to a dripping tap"></div>
    <div class="brand-mark"><span class="brand-mark__dot"></span><span class="brand-mark__name">Crestline<br>Gas &amp; Plumbing</span></div>
  </section>

  <section class="card card--back">
    <div class="pipe-art" role="img" aria-label="Faint illustration of plumbing pipes and a dripping tap"></div>
    <h1 class="contact-name">Dale Whitcombe</h1>
    <p class="contact-phone">Ph - 0455163027</p>
    <div class="brand-mark"><span class="brand-mark__dot"></span><span class="brand-mark__name">Crestline<br>Gas &amp; Plumbing</span></div>
    <h2 class="business-name">Crestline Gas &amp; Plumbing</h2>
    <p class="tagline">all types of plumbing and gas work and specialise<br>in general maintenance plumbing.</p>
    <p class="details">Email - admin@crestlinegasandplumbing.example.com.au<br>ABN - 68204915336</p>
  </section>
</main>
</body>
</html>
```